New Business Card Design Project

Need a design that will create an impact / strong impression towards our clients for our business. We are in the lighting business and we do lighting retrofits for large commercial to industrial clientele.

Target Market(s)

Lighting Industry

Industry/Entity Type

Business

Other font styles liked:
• we would like to use the font on our logo, not sure what it is though..

Requirements
Must have
• Our logo.
Nice to have
• We are open to suggestions that have to do with lighting.

```html
<!DOCTYPE html>
<html lang="en">
<head>
<meta charset="utf-8">
<title>Brightline Retrofit Group – Business Card</title>
<link href="https://fonts.googleapis.com/css2?family=Montserrat:wght@500;600&family=Open+Sans:wght@400&display=swap" rel="stylesheet">
<style>
  :root{
    --stage:#ecebe8;
    --paper:#ffffff;
    --green-deep:#0f3a12;
    --green-mid:#0a8a3c;
    --green-light:#6cc655;
    --green-name:#138a2f;
    --ink:#2b2b2b;
  }
  html,body{margin:0;padding:0;overflow:hidden;}
  body{width:1200px;height:900px;background:var(--stage);position:relative;}
  .card{position:absolute;overflow:hidden;box-shadow:0 6px 18px rgba(0,0,0,.18);}
  .card--front{left:177px;top:74px;width:589px;height:364px;background:var(--paper);}
  .card--back{left:388px;top:505px;width:567px;height:352px;background:var(--green-deep);}

  .brand{position:absolute;display:flex;align-items:center;gap:10px;
    font-family:"Montserrat",sans-serif;font-weight:600;letter-spacing:.04em;white-space:nowrap;}
  .brand__square{display:block;}
  .card--front .brand{left:28px;top:44px;font-size:21px;color:var(--green-deep);}
  .card--front .brand__square{width:16px;height:16px;background:var(--green-mid);}
  .card--back .brand{left:0;right:0;top:158px;justify-content:center;font-size:28px;color:var(--green-light);}
  .card--back .brand__square{width:22px;height:22px;background:var(--green-light);}

  .person{position:absolute;left:26px;top:145px;}
  .person__name{margin:0;font-family:"Montserrat",sans-serif;font-weight:600;font-size:20px;color:var(--green-name);letter-spacing:.01em;}
  .person__role{margin:2px 0 0;font-family:"Open Sans",sans-serif;font-size:15px;color:var(--ink);}

  .contact{position:absolute;left:26px;top:202px;margin:0;padding:0;list-style:none;
    font-family:"Open Sans",sans-serif;font-size:15px;color:var(--ink);}
  .contact li{display:flex;align-items:center;gap:8px;height:21.5px;}
  .contact svg{width:12px;height:12px;fill:var(--green-name);}
  .address{position:absolute;left:26px;top:274px;margin:0;font-family:"Open Sans",sans-serif;font-size:15px;line-height:22px;color:var(--ink);font-style:normal;}

  .accent{position:absolute;left:0;top:0;width:589px;height:364px;}
</style>
</head>
<body>
  <section class="card card--front">
    <svg class="accent" viewBox="0 0 589 364" aria-hidden="true">
      <polygon points="206,346 589,83 589,346" fill="var(--green-mid)"/>
      <rect x="0" y="346" width="589" height="18" fill="var(--green-mid)"/>
    </svg>

    <div class="brand"><span class="brand__square"></span>BRIGHTLINE RETROFIT GROUP</div>

    <div class="person">
      <h1 class="person__name">DANIEL REYES</h1>
      <p class="person__role">Managing Director</p>
    </div>

    <ul class="contact">
      <li><svg viewBox="0 0 24 24"><path d="M6.6 10.8a15.1 15.1 0 0 0 6.6 6.6l2.2-2.2c.3-.3.7-.4 1-.2 1.1.4 2.3.6 3.6.6.6 0 1 .4 1 1V20c0 .6-.4 1-1 1A17 17 0 0 1 3 4c0-.6.4-1 1-1h3.5c.6 0 1 .4 1 1 0 1.3.2 2.5.6 3.6.1.3 0 .7-.2 1z"/></svg>(044)123456789</li>
      <li><svg viewBox="0 0 24 24"><path d="M2 5h20v14H2z M4 7v.5l8 5 8-5V7l-8 5z" fill-rule="evenodd"/></svg>info@youremail.com</li>
      <li><svg viewBox="0 0 24 24"><circle cx="12" cy="12" r="10"/></svg>www.websitename.com</li>
    </ul>

    <address class="address">1234, Address GoesHere,<br>Country name, 12345</address>
  </section>

  <section class="card card--back">
    <div class="brand"><span class="brand__square"></span>BRIGHTLINE RETROFIT GROUP</div>
  </section>
</body>
</html>
```